Corporate Design für Sonderlösungen für Industrie und Handel
Zielgruppe
Wir entwickeln Sonderlösungen für Industrie und Handel. Unsere Kundschaft hat in der Regel ein existentes Problem oder eine Problemstellung, für das nach Lösungen gesucht wird. Hier kommen wir ins Spiel. Hauptsächlich sind diese Probleme im Bereich Logistik und Versand angesiedelt.
Aufgabenstellung
Hier sind sie relativ frei... das Corparate Indentity soll eine dynamische , moderne Komponente haben. Das Symsbol einen weitläufigen Bezug zu einem oder mehreren Begriffen wie Technik, Lösung , Logistik etc. haben.

```html
<!DOCTYPE html>
<html lang="de">
<head>
<meta charset="utf-8">
<title>Valtrano GmbH &amp; Co KG – Visitenkarte</title>
<link rel="stylesheet" href="https://fonts.googleapis.com/css2?family=Montserrat:wght@400;500;700&display=swap">
<style>
  :root {
    --bg: #d9dbde;
    --card: #ececec;
    --navy: #1d4f86;
    --blue: #2f9be0;
    --green: #1f9e4a;
    --grey-text: #3d3d3d;
    --bolt: #8a8a8a;
    --metal-light: #f1f2f3;
    --metal-mid: #c9ccd0;
    --metal-dark: #a8acb1;
  }
  * { box-sizing: border-box; margin: 0; padding: 0; }
  html, body { width: 1200px; height: 900px; overflow: hidden; }
  body {
    background: var(--bg);
    font-family: "Montserrat", sans-serif;
    display: flex;
    align-items: center;
    justify-content: center;
    gap: 40px;
  }
  .card {
    position: relative;
    width: 540px;
    height: 350px;
    box-shadow: 0 10px 24px rgba(0,0,0,.18);
    overflow: hidden;
  }

  /* Front side */
  .card-front { background: var(--metal-mid); }
  .metal-surface {
    position: absolute; inset: 0;
    background: linear-gradient(115deg, var(--metal-dark) 0%, var(--metal-light) 30%, var(--metal-mid) 55%, var(--metal-light) 78%, var(--metal-dark) 100%);
  }
  .screw {
    position: absolute; width: 14px; height: 14px; border-radius: 50%;
    background: radial-gradient(circle at 40% 35%, #f4f4f4, #7d7f82);
    border: 1px solid #6b6d70;
  }
  .screw.tl { top: 16px; left: 16px; } .screw.tr { top: 16px; right: 16px; }
  .screw.bl { bottom: 16px; left: 16px; } .screw.br { bottom: 16px; right: 16px; }
  .brand-front {
    position: absolute; inset: 0;
    display: flex; flex-direction: column; align-items: center; justify-content: center;
    color: var(--blue); font-weight: 700; line-height: 1;
  }
  .brand-front .brand-name { font-size: 62px; letter-spacing: 4px; }
  .brand-front .brand-legal { font-size: 24px; letter-spacing: 4px; margin-top: 12px; }

  /* Back side */
  .card-back { background: var(--card); border-bottom: 5px solid var(--navy); }
  .hex { position: absolute; width: 16px; height: 16px; }
  .hex.a { top: 22px; left: 18px; } .hex.b { top: 150px; left: 18px; }
  .hex.c { top: 160px; right: 18px; } .hex.d { bottom: 58px; right: 18px; }
  .brand-back {
    position: absolute; top: 20px; left: 46px;
    color: var(--blue); font-weight: 700; line-height: 1;
  }
  .brand-back .brand-name { font-size: 28px; letter-spacing: 2px; }
  .brand-back .brand-legal { font-size: 11px; letter-spacing: 2px; margin-top: 5px; display: block; }
  .accent-bar { position: absolute; width: 5px; height: 34px; background: var(--navy); }
  .accent-bar.left { top: 88px; left: 0; }
  .accent-bar.right { top: 150px; right: 0; }
  .person { position: absolute; top: 100px; left: 46px; }
  .person-name { color: var(--navy); font-weight: 700; font-size: 20px; }
  .person-role { color: var(--grey-text); font-size: 16px; margin-top: 2px; }
  .contact {
    position: absolute; top: 96px; right: 46px;
    list-style: none; text-align: right; color: var(--grey-text); font-size: 13.5px;
  }
  .contact li { display: flex; align-items: center; justify-content: flex-end; gap: 10px; margin-bottom: 8px; }
  .contact .address { align-items: flex-start; line-height: 1.25; }
  .contact .company { color: var(--navy); font-weight: 700; display: block; }
  .icon { width: 18px; height: 18px; flex: none; }
  .info-band {
    position: absolute; left: 0; right: 0; bottom: 0; height: 40px;
    background: var(--green); color: #fff;
    font-size: 12px; font-weight: 700; letter-spacing: .5px;
    display: flex; align-items: center; padding-left: 46px;
  }
</style>
</head>
<body>

<section class="card card-front">
  <div class="metal-surface" role="img" aria-label="Gebürstete Metallstruktur"></div>
  <span class="screw tl"></span><span class="screw tr"></span>
  <span class="screw bl"></span><span class="screw br"></span>
  <div class="brand-front">
    <span class="brand-name">VALTRANO</span>
    <span class="brand-legal">GmbH &amp; Co KG</span>
  </div>
</section>

<section class="card card-back">
  <svg class="hex a" viewBox="0 0 16 16"><polygon points="4,1 12,1 16,8 12,15 4,15 0,8" fill="var(--bolt)"/><circle cx="8" cy="8" r="3" fill="#bcbcbc"/></svg>
  <svg class="hex b" viewBox="0 0 16 16"><polygon points="4,1 12,1 16,8 12,15 4,15 0,8" fill="var(--bolt)"/><circle cx="8" cy="8" r="3" fill="#bcbcbc"/></svg>
  <svg class="hex c" viewBox="0 0 16 16"><polygon points="4,1 12,1 16,8 12,15 4,15 0,8" fill="var(--bolt)"/><circle cx="8" cy="8" r="3" fill="#bcbcbc"/></svg>
  <svg class="hex d" viewBox="0 0 16 16"><polygon points="4,1 12,1 16,8 12,15 4,15 0,8" fill="var(--bolt)"/><circle cx="8" cy="8" r="3" fill="#bcbcbc"/></svg>

  <div class="brand-back">
    <span class="brand-name">VALTRANO</span>
    <span class="brand-legal">GmbH &amp; Co KG</span>
  </div>

  <span class="accent-bar left"></span>
  <span class="accent-bar right"></span>

  <div class="person">
    <p class="person-name">Karim ALDOUS</p>
    <p class="person-role">Geschäftsführer</p>
  </div>

  <ul class="contact">
    <li class="address">
      <span><span class="company">Valtrano GmbH &amp; Co KG</span>Lindenweg 12<br>10115, Musterstadt, Germany</span>
      <svg class="icon" viewBox="0 0 18 18"><circle cx="9" cy="9" r="9" fill="var(--green)"/><path d="M9 4a3 3 0 0 0-3 3c0 2.3 3 6 3 6s3-3.7 3-6a3 3 0 0 0-3-3z" fill="#fff"/><circle cx="9" cy="7" r="1.1" fill="var(--green)"/></svg>
    </li>
    <li>+49 (0)123 456 78 90
      <svg class="icon" viewBox="0 0 18 18"><circle cx="9" cy="9" r="9" fill="var(--green)"/><path d="M6 4.5l2 2-1 1.3a6 6 0 0 0 3.2 3.2l1.3-1 2 2-1.2 1.5C8.6 13.2 4.8 9.4 4.5 5.7z" fill="#fff"/></svg>
    </li>
    <li>kontakt@valtrano.example
      <svg class="icon" viewBox="0 0 18 18"><circle cx="9" cy="9" r="9" fill="var(--green)"/><rect x="4.5" y="5.5" width="9" height="7" fill="#fff"/><path d="M4.5 5.5L9 9.5l4.5-4" fill="none" stroke="var(--green)" stroke-width="1"/></svg>
    </li>
    <li>www.valtrano.example
      <svg class="icon" viewBox="0 0 18 18"><circle cx="9" cy="9" r="9" fill="var(--green)"/><circle cx="9" cy="9" r="4.8" fill="none" stroke="#fff" stroke-width="1.2"/><path d="M4.2 9h9.6M9 4.2c-2 2.6-2 7 0 9.6M9 4.2c2 2.6 2 7 0 9.6" fill="none" stroke="#fff" stroke-width="1"/></svg>
    </li>
    <li>netz.example/in/valtrano
      <svg class="icon" viewBox="0 0 18 18"><circle cx="9" cy="9" r="9" fill="var(--green)"/></svg>
    </li>
  </ul>

  <div class="info-band">INFORMATION ABOUT YOUR COMPANY</div>
</section>

</body>
</html>
```